Silver Heron Motor Works needs a logo design

I'm after a logo design for a new Female owned automotive repair workshop in the Queanbeyan/Canberra Australia Area.
We offer repairs on all passenger cars, 4wds and light trucks emphasising a strong honest work ethic and a genuine interest in the customer and their vehicles needs. With business details on the front of the card and what we offer on the back.
I would like a design with a phoenix in multiple colours maybe hovering over a flaming wheel or a car with wheels flaming with the phoenix hovering up out of the flames
Target Market(s)
All Vehicle users
Industry/Entity Type
Automotive
Contact Information for Business Card
On the front
Silver Heron Motor
Marla Pettigrew Owner/ Mechanic 0471385026
email marla@silverheronmotor.com.au
Website www.silverheronmotorworks.com.au
On the back
All Cars, 4WDs, Light trucks, makes and models
Log book servicing
General vehicle servicing
Major vehicle servicing
brake and clutch servicing and repairs
Suspension repairs
cooling systems
All major and minor mechanical repairs
minor electrical rewiring and repairs
Colors
Designer to choose colors to be used in the design.
Look and feel

```html
<!DOCTYPE html>
<html lang="en">
<head>
<meta charset="utf-8">
<title>Silver Heron Motor – Business Card</title>
<link rel="stylesheet" href="https://fonts.googleapis.com/css2?family=Open+Sans:wght@400;600;700&display=swap">
<style>
  :root{
    --stage:#e9e4dc;
    --card-dark:#262626;
    --card-light:#ffffff;
    --ink:#2b2b2b;
    --ink-soft:#555555;
    --text-light:#e6e6e6;
    --accent:#f2763a;
    --accent-deep:#e8542f;
    --violet:#6a3fd1;
    --magenta:#d8367f;
    --teal:#1fb7a8;
  }
  *{box-sizing:border-box;margin:0;padding:0}
  html,body{width:1200px;height:800px;overflow:hidden}
  body{
    background:var(--stage);
    font-family:"Open Sans",Arial,sans-serif;
    display:flex;align-items:center;justify-content:center;gap:40px;
  }
  .card{
    position:relative;width:560px;height:320px;border-radius:18px;overflow:hidden;
    box-shadow:0 10px 28px rgba(0,0,0,.18);
  }

  /* Back: services */
  .card--back{background:var(--card-dark);color:var(--text-light)}
  .services{
    position:absolute;left:40px;top:70px;list-style:none;
    font-size:15px;line-height:25px;
  }
  .services li{display:flex;align-items:center;gap:10px}
  .tick{width:14px;height:14px;flex:none}
  .brand{
    position:absolute;display:flex;align-items:center;gap:10px;
    font-weight:700;letter-spacing:.02em;white-space:nowrap;
  }
  .brand__dot{border-radius:50%;background:var(--accent);flex:none}
  .card--back .brand{right:36px;top:140px;font-size:22px;color:#ffffff}
  .card--back .brand__dot{width:16px;height:16px}

  /* Front: contact */
  .card--front{background:var(--card-light);color:var(--ink)}
  .artwork{
    position:absolute;right:-30px;top:-20px;width:330px;height:360px;
    border-radius:50% 40% 45% 55%;
    background:linear-gradient(200deg,var(--accent) 0%,var(--accent-deep) 30%,var(--magenta) 55%,var(--violet) 78%,var(--teal) 100%);
    opacity:.85;filter:blur(6px);
  }
  .card--front .brand{left:36px;top:46px;font-size:19px;color:var(--ink)}
  .card--front .brand__dot{width:14px;height:14px}
  .person{position:absolute;left:36px;top:130px}
  .person__name{font-size:30px;font-weight:400;color:var(--ink-soft);line-height:1.1}
  .person__name strong{font-weight:700;color:var(--ink)}
  .person__role{font-size:15px;color:var(--accent);margin-top:4px}
  .contact{position:absolute;left:36px;top:222px;list-style:none;font-size:14px;line-height:26px;color:var(--ink)}
  .contact li{display:flex;align-items:center;gap:10px}
  .contact svg{width:14px;height:14px;flex:none}
</style>
</head>
<body>

  <section class="card card--back" aria-label="Card back: services">
    <ul class="services">
      <li><svg class="tick" viewBox="0 0 14 14"><rect x="0.5" y="0.5" width="13" height="13" rx="2" fill="none" stroke="#f2763a"/><path d="M3 7.5l3 3 5-7" fill="none" stroke="#f2763a" stroke-width="2"/></svg>All Cars, 4WDs, Light trucks, makes and models</li>
      <li><svg class="tick" viewBox="0 0 14 14"><rect x="0.5" y="0.5" width="13" height="13" rx="2" fill="none" stroke="#f2763a"/><path d="M3 7.5l3 3 5-7" fill="none" stroke="#f2763a" stroke-width="2"/></svg>All Servicing</li>
      <li><svg class="tick" viewBox="0 0 14 14"><rect x="0.5" y="0.5" width="13" height="13" rx="2" fill="none" stroke="#f2763a"/><path d="M3 7.5l3 3 5-7" fill="none" stroke="#f2763a" stroke-width="2"/></svg>Brake and clutch servicing and repairs</li>
      <li><svg class="tick" viewBox="0 0 14 14"><rect x="0.5" y="0.5" width="13" height="13" rx="2" fill="none" stroke="#f2763a"/><path d="M3 7.5l3 3 5-7" fill="none" stroke="#f2763a" stroke-width="2"/></svg>Suspension repairs</li>
      <li><svg class="tick" viewBox="0 0 14 14"><rect x="0.5" y="0.5" width="13" height="13" rx="2" fill="none" stroke="#f2763a"/><path d="M3 7.5l3 3 5-7" fill="none" stroke="#f2763a" stroke-width="2"/></svg>Cooling systems</li>
      <li><svg class="tick" viewBox="0 0 14 14"><rect x="0.5" y="0.5" width="13" height="13" rx="2" fill="none" stroke="#f2763a"/><path d="M3 7.5l3 3 5-7" fill="none" stroke="#f2763a" stroke-width="2"/></svg>All major and minor mechanical repairs</li>
      <li><svg class="tick" viewBox="0 0 14 14"><rect x="0.5" y="0.5" width="13" height="13" rx="2" fill="none" stroke="#f2763a"/><path d="M3 7.5l3 3 5-7" fill="none" stroke="#f2763a" stroke-width="2"/></svg>Minor electrical rewiring and repairs</li>
    </ul>
    <div class="brand" style="top:24px;right:32px;font-size:18px"><span class="brand__dot"></span>Silver Heron Motor</div>
  </section>

  <section class="card card--front" aria-label="Card front: contact details">
    <div class="artwork" role="img" aria-label="Large multicoloured rising bird illustration in orange, magenta, violet and teal"></div>
    <div class="brand"><span class="brand__dot"></span>Silver Heron Motor</div>
    <div class="person">
      <h1 class="person__name">Marla <strong>Pettigrew</strong></h1>
      <p class="person__role">Owner | Mechanic</p>
    </div>
    <ul class="contact">
      <li><svg viewBox="0 0 14 14"><path d="M3 1h2.5l1 3-1.5 1.2a8 8 0 0 0 3.8 3.8L10 7.5l3 1V11a2 2 0 0 1-2 2A10 10 0 0 1 1 3a2 2 0 0 1 2-2z" fill="#f2763a"/></svg>0471385026</li>
      <li><svg viewBox="0 0 14 14"><rect x="1" y="3" width="12" height="8.5" rx="1" fill="#f2763a"/><path d="M1.5 3.5L7 8l5.5-4.5" fill="none" stroke="#fff" stroke-width="1.2"/></svg>email marla@silverheronmotor.com.au</li>
    </ul>
  </section>

</body>
</html>
```